Modern Billboard Ad for Criminal Defense Firm

10.5 x 36 We're looking for something to set us apart from the local competition. Looking for sleek and modern. We're a mid-sized firm in a small market city. We want to give the artist room to be creative on this one.
Thanks

Target Market(s)

Adult clients who have been charged with a crime/DWI

Industry/Entity Type

legal

Font styles to use
Serif
Sans Serif

Requirements
Must have
• Needs to have the firm name in large lettering. Law Offices of Marcus T Whitfield. “PLLC” does not have to be included. Phone number of (555) 384-1927 should be included but not the main focus.
Nice to have
• A call to action or something similar. “Don’t go it alone, call today.”, “ Arrested?”

```html
<!DOCTYPE html>
<html lang="en">
<head>
<meta charset="UTF-8">
<title>Law Offices of Marcus T Whitfield – Billboard</title>
<link href="https://fonts.googleapis.com/css2?family=Montserrat:ital,wght@0,500;0,600;0,700;1,600;1,800&display=swap" rel="stylesheet">
<style>
  :root {
    --brand-blue: #0e4fb0;
    --ink-blue: #0c3e94;
    --paper: #ffffff;
    --stage: #e9ecf1;
    --photo-light: #eef1f5;
    --photo-mid: #b9bfc8;
    --badge-dark: #1c2430;
    --badge-accent: #2fa8e6;
  }
  * { margin: 0; padding: 0; box-sizing: border-box; }
  html, body { width: 1200px; height: 900px; overflow: hidden; }
  body {
    background: var(--stage);
    font-family: "Montserrat", Arial, sans-serif;
    position: relative;
  }
  .billboard {
    position: absolute;
    left: 40px; top: 280px;
    width: 1120px; height: 340px;
    background: var(--paper);
    overflow: hidden;
    box-shadow: 0 10px 30px rgba(20, 40, 80, 0.12);
  }
  .billboard-shapes { position: absolute; inset: 0; }
  .headline {
    position: absolute;
    left: 62px; top: 92px;
    color: var(--ink-blue);
  }
  .headline-cta {
    font-style: italic;
    font-weight: 600;
    font-size: 32px;
    line-height: 40px;
    letter-spacing: -0.5px;
  }
  .headline-main {
    font-style: italic;
    font-weight: 800;
    font-size: 62px;
    line-height: 70px;
    letter-spacing: -1px;
    margin-left: -4px;
  }
  .firm-panel {
    position: absolute;
    left: 816px; top: 193px;
    width: 284px;
    color: var(--paper);
    text-align: center;
  }
  .firm-name {
    border: 2px solid var(--paper);
    padding: 7px 6px 6px;
  }
  .firm-name-prefix { font-weight: 500; font-size: 19px; line-height: 22px; }
  .firm-name-main { font-weight: 700; font-size: 22px; line-height: 28px; letter-spacing: 0.2px; }
  .firm-phone {
    margin-top: 12px;
    font-weight: 600;
    font-size: 26px;
    letter-spacing: 0.5px;
  }
</style>
</head>
<body>
  <section class="billboard" aria-label="Criminal defense billboard">
    <svg class="billboard-shapes" width="1120" height="340" viewBox="0 0 1120 340" aria-hidden="false">
      <polygon class="corner-band" points="0,0 232,0 0,83" fill="var(--brand-blue)"/>
      <polygon class="base-wedge" points="307,340 433,290 433,340" fill="var(--brand-blue)"/>
      <polygon class="portrait-wedge" points="674,197 762,151 762,340" fill="var(--brand-blue)"/>
      <defs>
        <linearGradient id="portraitTone" x1="0" y1="0" x2="0" y2="1">
          <stop offset="0" stop-color="var(--photo-light)"/>
          <stop offset="0.55" stop-color="#d9dde3"/>
          <stop offset="1" stop-color="var(--photo-mid)"/>
        </linearGradient>
      </defs>
      <rect class="attorney-portrait" x="466" y="0" width="296" height="340" fill="url(#portraitTone)" role="img" aria-label="Portrait photo of the attorney in a grey suit and tie"/>
      <polygon class="firm-block" points="796,340 796,116 1120,0 1120,340" fill="var(--brand-blue)"/>
      <g class="award-badge">
        <rect x="909" y="29" width="97" height="141" fill="var(--badge-dark)"/>
        <rect x="909" y="29" width="97" height="28" fill="var(--badge-accent)"/>
        <rect x="909" y="150" width="97" height="20" fill="var(--badge-accent)"/>
      </g>
    </svg>

    <div class="headline">
      <p class="headline-cta">DON’T GO IT ALONE,<br>CALL TODAY</p>
      <p class="headline-main">ARRESTED?</p>
    </div>

    <div class="firm-panel">
      <div class="firm-name">
        <p class="firm-name-prefix">LAW OFFICES OF</p>
        <p class="firm-name-main">MARCUS T WHITFIELD</p>
      </div>
      <p class="firm-phone">(555) 384-1927</p>
    </div>
  </section>
</body>
</html>
```